Pool Screen Enclosure Building a Career Boot Camp!

Looking to Host a Boot Camp for people looking for a career or looking to change careers. We Design, Manufacture and Install Custom Pool Screen Enclosures. We have a training program to allow Non Experienced motivated people the chance at a great career that will provide a great living for them and their family. This will be a paid boot camp, week long, we provide all the initial training for them to make a transition into our business. This will be 5 days of training with a guaranteed job to start the following Monday.... This is good for both someone with no construction experience or someone with construction experience that wants to upgrade their current job.
Paid Boot Camp
transition to a full time job with great pay
Benefits include Health Insurance, Dental and Vision, 401K, we provide the tools and training.

```html
<!DOCTYPE html>
<html lang="en">
<head>
<meta charset="utf-8">
<title>Paid Boot Camp Flyer</title>
<link href="https://fonts.googleapis.com/css2?family=Montserrat:wght@400;500;600;700;800&display=swap" rel="stylesheet">
<style>
  :root{
    --green:#6cbd45;
    --green-dark:#4f9e2c;
    --yellow:#f9bf1e;
    --black:#0b0b0b;
    --paper:#f4f5f3;
    --white:#ffffff;
    --ink:#111111;
    --rule:#2a2a2a;
  }
  *{margin:0;padding:0;box-sizing:border-box}
  html,body{width:950px;height:1200px;overflow:hidden;background:var(--paper)}
  body{font-family:'Montserrat',sans-serif;color:var(--ink)}
  .flyer{position:relative;width:950px;height:1200px;overflow:hidden;
    background:linear-gradient(180deg,#ffffff 45%,#e9ebe8 100%)}
  .top-stripe{position:absolute;left:0;top:0;width:950px;height:20px;background:var(--green)}
  .header{position:absolute;left:0;top:20px;width:950px;height:137px;background:var(--black);
    display:flex;align-items:center;justify-content:center;gap:14px}
  .brand-dot{width:46px;height:46px;border-radius:50%;background:var(--green)}
  .brand-name{font-weight:700;font-size:36px;color:var(--green);letter-spacing:.3px}
  .hero{position:absolute;left:0;top:157px;width:950px;height:407px;
    background:linear-gradient(180deg,#3b3d3c 0%,#8f9496 30%,#b9bcbd 55%,#6f7469 72%,#3f5a4d 85%,#2f3f44 100%)}
  .headline{position:absolute;left:0;top:420px;width:584px;height:58px;background:var(--green);
    font-weight:800;font-size:52px;line-height:58px;padding-left:38px;color:var(--black);letter-spacing:.5px}
  .subhead{position:absolute;left:0;top:478px;width:765px;height:37px;background:var(--yellow);
    font-weight:500;font-size:30px;line-height:37px;padding-left:38px;color:var(--black)}
  .thumb{position:absolute;top:547px;width:160px;height:185px;background:var(--white);padding:5px;
    border-radius:6px;box-shadow:0 4px 10px rgba(0,0,0,.25)}
  .thumb div{width:100%;height:100%;border-radius:3px}
  .thumb-team{left:14px}
  .thumb-team div{background:linear-gradient(180deg,#d7d4cd,#bcb3a4)}
  .thumb-install{left:188px}
  .thumb-install div{background:linear-gradient(180deg,#4f86c6 0%,#a8c3de 45%,#7b7f82 100%)}
  .thumb-frame{left:362px}
  .thumb-frame div{background:linear-gradient(180deg,#bfc3c6 0%,#8e9294 55%,#6d6a5d 100%)}
  .about{position:absolute;left:546px;top:579px;width:404px;height:520px;background:var(--green);
    border-radius:14px 0 0 14px;padding:23px 18px 0 23px;color:var(--white);
    font-size:14.6px;line-height:23.5px;font-weight:400}
  .about p+p{margin-top:23px}
  .about strong{font-weight:700}
  .benefits{position:absolute;left:40px;top:778px;width:463px;height:289px;
    border:2px dashed var(--green);border-radius:10px;padding:12px 16px 0 16px;background:var(--white);
    box-shadow:0 14px 14px -12px rgba(0,0,0,.35)}
  .benefits-title{font-weight:800;font-size:26px;color:var(--green);text-decoration:underline;
    text-decoration-thickness:2px;text-underline-offset:3px}
  .benefits-title span{color:var(--yellow)}
  .benefit-list{list-style:none;margin-top:10px}
  .benefit-list li{display:flex;align-items:center;gap:8px;font-weight:600;font-size:20.5px;
    height:57px;border-bottom:1.5px solid var(--rule);width:275px;white-space:nowrap}
  .benefit-list li:last-child{border-bottom:none;width:auto}
  .benefit-list li:first-child{height:40px;align-items:flex-start;padding-top:4px}
  .tick{flex:none;width:17px;height:17px}
  .footer{position:absolute;left:0;top:1125px;width:950px;height:54px}
  .footer svg{position:absolute;left:0;top:0}
  .address{position:absolute;left:78px;top:1133px;font-weight:700;font-size:16.5px;line-height:20px;color:var(--black)}
  .contact{position:absolute;left:410px;top:1125px;height:54px;display:flex;align-items:center;gap:14px;color:var(--black)}
  .phone{font-weight:800;font-size:25px}
  .divider{width:3px;height:26px;background:var(--black)}
  .email{font-weight:700;font-size:15.5px}
</style>
</head>
<body>
<div class="flyer">
  <div class="top-stripe"></div>
  <header class="header">
    <div class="brand-dot"></div>
    <div class="brand-name">Lanai Works</div>
  </header>

  <div class="hero" role="img" aria-label="Photo of a finished dark-framed pool screen enclosure over a pool, overlooking a lake under a cloudy sky"></div>
  <h1 class="headline">PAID BOOT CAMP</h1>
  <div class="subhead">Transition to a full time job with great pay</div>

  <div class="thumb thumb-team"><div role="img" aria-label="Photo of trainees reviewing enclosure plans on the ground"></div></div>
  <div class="thumb thumb-install"><div role="img" aria-label="Photo of workers installing an enclosure frame on a house"></div></div>
  <div class="thumb thumb-frame"><div role="img" aria-label="Photo of a worker on a ladder fitting enclosure screens"></div></div>

  <section class="about">
    <p>Looking to Host a Boot Camp for people looking for a career or looking to change careers. We <strong>Design, Manufacture</strong> and <strong>Install Custom Pool Screen Enclosures</strong>. We have a <strong>training program</strong> to allow <strong>Non Experienced motivated people</strong> the chance at a great career that will provide a great living for them and their family.</p>
    <p>This will be a <strong>PAID BOOT CAMP</strong>, week long, we provide all the initial training for them to make a transition into our business. This will be <strong>5 DAYS</strong> of training with a <strong>GUARANTEED JOB</strong> to start the following Monday....</p>
    <p>This is good for both someone with no <strong>CONSTRUCTION EXPERIENCE</strong> or someone with construction experience that wants to upgrade their current job.</p>
  </section>

  <section class="benefits">
    <h2 class="benefits-title">BENEFITS <span>INCLUDE:</span></h2>
    <ul class="benefit-list">
      <li><svg class="tick" viewBox="0 0 20 20"><circle cx="10" cy="10" r="8.5" fill="none" stroke="#6cbd45" stroke-width="2"/><path d="M5.5 10.5l3 3 6-7" fill="none" stroke="#6cbd45" stroke-width="2.4" stroke-linecap="round" stroke-linejoin="round"/></svg>Health Insurance</li>
      <li><svg class="tick" viewBox="0 0 20 20"><circle cx="10" cy="10" r="8.5" fill="none" stroke="#6cbd45" stroke-width="2"/><path d="M5.5 10.5l3 3 6-7" fill="none" stroke="#6cbd45" stroke-width="2.4" stroke-linecap="round" stroke-linejoin="round"/></svg>Dental and Vision</li>
      <li><svg class="tick" viewBox="0 0 20 20"><circle cx="10" cy="10" r="8.5" fill="none" stroke="#6cbd45" stroke-width="2"/><path d="M5.5 10.5l3 3 6-7" fill="none" stroke="#6cbd45" stroke-width="2.4" stroke-linecap="round" stroke-linejoin="round"/></svg>401K</li>
      <li><svg class="tick" viewBox="0 0 20 20"><circle cx="10" cy="10" r="8.5" fill="none" stroke="#6cbd45" stroke-width="2"/><path d="M5.5 10.5l3 3 6-7" fill="none" stroke="#6cbd45" stroke-width="2.4" stroke-linecap="round" stroke-linejoin="round"/></svg>We provide the tools and training</li>
    </ul>
  </section>

  <footer class="footer">
    <svg width="950" height="54" viewBox="0 0 950 54">
      <polygon points="0,0 378,0 352,54 0,54" fill="#6cbd45"/>
      <polygon points="392,0 950,0 950,54 366,54" fill="#f9bf1e"/>
    </svg>
  </footer>
  <div class="address">418 W HARBOR AVENUE,<br>PORT SABLE FL 34990</div>
  <div class="contact">
    <span class="phone">555-201-4478</span>
    <span class="divider"></span>
    <span class="email">Admin@lanaiworks-example.com</span>
  </div>
</div>
</body>
</html>
```